Thank You Card design for a federal credit union

I am looking to have a thank you card designed.
Specs:
Flat size of 9.5"x6.5" folds to final size of 4.75"x6.5", it will print full color on the front and back. Below, you will see their logo, which needs to print on the inside of the folded card. I also attached images of their current card. They would like to keep the blue color but are open to design on the front. This is a Federal Credit Union, so please make the design, modern and professional. Below is the text that needs to print below the logo on the inside of the card. The text and logo will print below the fold on the inside, leave the top portion (above the panel) white.
Inside text:
Our Members are the foundation of our Credit Union. We sincerely thank you for your loyalty, your business and the opportunity to serve you.
Target Market(s)
Clients of a federal credit union
Industry/Entity Type
Union
Requirements
Must have
- a simple, professional, and modern feel. "Thank You for your business" must be on the front section in some variation.
Should not have
- nothing flashy or too many colors. keep it simple

```html
<!DOCTYPE html>
<html lang="en">
<head>
<meta charset="utf-8">
<title>Thank You Card – Folded Layout</title>
<link href="https://fonts.googleapis.com/css2?family=Arimo:wght@700&family=Source+Sans+3:wght@400&family=Pinyon+Script&display=swap" rel="stylesheet">
<style>
  :root {
    --canvas: #e6e7e8;
    --label: #2e3192;
    --paper: #ffffff;
    --navy-deep: #201d5a;
    --navy-glow: #3a40a0;
    --ink: #25215f;
    --frame-line: #c4c6ce;
    --frame-tint: #f1f1f4;
    --card-edge: #5b5ea6;
    --gold-light: #ffcf3a;
    --gold-dark: #f0a21a;
  }
  * { margin: 0; padding: 0; box-sizing: border-box; }
  html, body { width: 1200px; height: 800px; overflow: hidden; }
  body { background: var(--canvas); position: relative; font-family: "Arimo", Arial, sans-serif; }

  .view-label, .panel-label {
    position: absolute;
    font-family: "Source Sans 3", "Myriad Pro", sans-serif;
    font-size: 17px;
    line-height: 20px;
    color: var(--label);
  }
  .view-label { top: 34px; transform: translateX(-50%); }
  .view-label.outside { left: 315px; }
  .view-label.inside { left: 891px; }
  .panel-label.back { left: 83px; top: 192px; }
  .panel-label.front { left: 83px; top: 458px; }
  .panel-label.first { left: 1101px; top: 205px; }
  .panel-label.last { left: 1101px; top: 471px; }

  .card-outside {
    position: absolute; left: 172px; top: 85px; width: 348px; height: 508px;
    border: 1px solid var(--card-edge); background: var(--paper);
  }
  .card-outside .back-panel { height: 254px; border-bottom: 1px solid var(--card-edge); }
  .card-outside .front-panel {
    position: relative; height: 252px;
    background: radial-gradient(ellipse 60% 62% at 50% 50%, var(--navy-glow) 0%, #2b2d80 45%, var(--navy-deep) 100%);
    color: var(--paper); text-align: center;
  }
  .ornament-area {
    position: absolute; left: 50%; width: 34px; height: 34px; transform: translateX(-50%);
    background: linear-gradient(160deg, var(--gold-light), var(--gold-dark));
  }
  .ornament-area.top { top: 43px; }
  .ornament-area.bottom { top: 183px; }
  .front-message { position: absolute; top: 90px; left: 0; right: 0; }
  .front-message .lead { font-size: 9.5px; line-height: 14px; font-weight: 700; }
  .front-message .headline {
    font-family: "Pinyon Script", cursive; font-size: 36px; line-height: 36px;
    text-shadow: 2px 3px 4px rgba(0,0,0,0.45);
  }
  .front-message .tail { font-size: 8.5px; line-height: 12px; font-weight: 700; margin-top: 8px; }

  .card-inside {
    position: absolute; left: 722px; top: 94px; width: 343px; height: 502px; background: var(--paper);
  }
  .card-inside .panel-frame { position: absolute; left: 0; top: 0; }
  .inside-content { position: absolute; top: 283px; left: 0; right: 0; text-align: center; color: var(--ink); }
  .brand-mark { display: flex; justify-content: center; align-items: center; gap: 6px; height: 44px; margin-left: 18px; }
  .brand-mark .brand-square { width: 14px; height: 14px; background: var(--ink); }
  .brand-mark .brand-name { font-size: 14px; font-weight: 700; line-height: 16px; }
  .inside-message {
    margin: 14px auto 0; width: 246px;
    font-size: 8.3px; line-height: 12.5px; font-weight: 700;
  }
</style>
</head>
<body>
  <div class="view-label outside">OUTSIDE</div>
  <div class="view-label inside">INSIDE</div>
  <div class="panel-label back">BACK</div>
  <div class="panel-label front">FRONT</div>
  <div class="panel-label first">FIRST</div>
  <div class="panel-label last">LAST</div>

  <section class="card-outside">
    <div class="back-panel"></div>
    <div class="front-panel">
      <div class="ornament-area top" role="img" aria-label="Golden autumn leaf ornament"></div>
      <div class="front-message">
        <p class="lead">WE<br>WOULD LIKE TO SAY</p>
        <p class="headline">Thank You</p>
        <p class="tail">FOR YOUR BUSSINESS</p>
      </div>
      <div class="ornament-area bottom" role="img" aria-label="Golden autumn leaf ornament"></div>
    </div>
  </section>

  <section class="card-inside">
    <svg class="panel-frame" width="343" height="502" viewBox="0 0 343 502" fill="none">
      <g stroke="var(--frame-line)" stroke-width="1">
        <polyline points="128,257 3,257 3,497 128,497"/>
        <polyline points="214,257 338,257 338,497 214,497"/>
      </g>
      <g fill="var(--frame-tint)">
        <rect x="9" y="305" width="10" height="145" role="img" aria-label="Decorative side ornament"/>
        <rect x="324" y="305" width="10" height="145" role="img" aria-label="Decorative side ornament"/>
      </g>
    </svg>
    <div class="inside-content">
      <div class="brand-mark">
        <span class="brand-square"></span>
        <span class="brand-name">Northgate</span>
      </div>
      <p class="inside-message">Our Members are the foundation of our Credit Union. We sincerely thank you for your loyalty, your business and the opportunity to serve you.</p>
    </div>
  </section>
</body>
</html>
```